Clean energy startup needs brochure & datasheet

• We are a solar energy start-up providing solar hybrid solutions for off-grid power demand. We need a brochure for our flagship product: our modular, transportable solar power generator, which can be installed in addition to diesel generators or batteries.
• Please visit our website www.solvantix.com to get a better feel for what we do.
• The goal of this brochure is to explain how our solar generator works and that Solvantix provides 2 different types of systems (solar-diesel and solar-battery), according to the customer needs.
• Size of the brochure (each page) is A4
• It will mostly be sent by email, so all pages should look good even if the viewer can see only one page (no graphics spanning several pages)
• A key challenge is the very high density of information on our pages - the color scheme should help in separating the main points and highlight the main conclusions
Updates

Project Deadline Extended
Reason: We still have multiple designs under consideration and need more time to work out the details.

Project Deadline Extended
Reason: We are getting close ! We were quite late in giving feedback last week, sorry for that. Thus, we give you some more time to finalise your job. Good luck !

Target Market(s)

Potential customers, meaning people all the way from diesel technicians to executives working in various sectors (prime markets are mining, light industry, construction, utilities, real estate,…)

Industry/Entity Type

Solar Energy

Font styles to use
Serif
Sans Serif

Requirements
Must have
• • Design a clean, easy to read, 4 page-brochure (A4 format bifold) with general explanations of the systems (see attached file 6 for the content and some layout ideas)
• Design one inlay datasheet (A4 double sided) with some specific technical specs of the various equipment sizes, to added in the brochure (see attached file 6 for the content and some layout ideas)
• Use Solvantix logo and derive a color scheme from our logos (there are several versions in orange, gray and white, allowing a choice of potential color schemes)
• Designers should propose multiple backgrounds for our solar generator pictures (the files with solar racking with a currently transparent background), e.g. Middle East (Desert) / Africa (Savannah) / Afghanistan (Mountains)
• Ability to edit raw files in Adobe Illustrator / Photoshop (please check with us if you want to use another program)

Nice to have
• • Provision to change pictures later (as we get real pictures from our demo plants)
Should not have
• • Any images or allusions to wind power, biomass, or other forms of renewable energy that are not solar
• Any images or allusions to green European looking landscapes (lawns, green trees, etc.) - this is a product for the Middle East & Africa!
• Any images or allusions to people in suits - this is an industrial product

```html
<!DOCTYPE html>
<html lang="en">
<head>
<meta charset="utf-8">
<title>Solvantix – Solar Generator Brochure Spread</title>
<link href="https://fonts.googleapis.com/css2?family=Arimo:ital,wght@0,400;0,700;1,700&display=swap" rel="stylesheet">
<style>
:root{
  --bg:#e9e6e1;
  --paper:#ffffff;
  --ink:#1c1c1c;
  --orange:#f0a23c;
  --yellow:#f7c51d;
  --heat0:#3fae49;
  --heat1:#d6e34c;
  --heat2:#f7d25a;
  --heat3:#f6a35a;
  --heat4:#f07f6a;
  --heat5:#e65a55;
  --head:#dcdcdc;
  --total:#d6eef7;
  --grid:#9a9a9a;
}
*{box-sizing:border-box;margin:0;padding:0}
html,body{width:1200px;height:864px;overflow:hidden;background:var(--bg);font-family:"Arimo",Arial,sans-serif;color:var(--ink)}
.spread{position:absolute;left:27px;top:25px;width:1145px;height:813px}
.page-left{position:absolute;left:0;top:0;width:575px;height:813px;background:var(--paper)}
.page-right{position:absolute;left:575px;top:0;width:570px;height:813px;overflow:hidden}
.section-title{position:absolute;font-weight:700;font-style:italic;font-size:18px;text-align:center;width:575px;left:0}
.config-title{top:24px}
.daily-title{top:416px}
.config-table{position:absolute;left:36px;top:60px;width:497px;border-collapse:collapse;font-size:10px;table-layout:fixed}
.config-table td{border:1px solid var(--orange);padding:1px 5px;vertical-align:middle;line-height:1.2}
.config-table td:first-child{white-space:nowrap}
.config-table td:not(:first-child){text-align:center}
.config-table .indent{padding-left:12px}
.config-table th{font-weight:400;font-size:10px;border:1px solid var(--orange);padding:2px}
.config-table sub,.config-table sup{font-size:7px;line-height:0}
.config-table .blank td{height:12px}
.notes{position:absolute;left:130px;top:328px;font-size:11px;line-height:14px;list-style:none}
.notes li{position:relative;padding-left:12px;margin-bottom:6px;width:300px}
.notes li::before{content:"";position:absolute;left:0;top:5px;width:4px;height:4px;border-radius:50%;background:var(--ink)}
.block-label{position:absolute;left:33px;top:452px;font-size:11px}
.kwh-label{position:absolute;left:31px;top:469px;font-size:5px}
.heat{position:absolute;left:31px;top:479px;width:510px;border-collapse:collapse;font-size:5px;table-layout:fixed}
.heat td,.heat th{border:1px solid var(--grid);height:15px;text-align:center;font-weight:400;background:var(--heat0);overflow:hidden;white-space:nowrap}
.heat th{background:var(--head)}
.heat th.time{background:#d0312d;color:#fff}
.heat .month{background:#fff;text-align:left;padding-left:2px}
.heat .sum{background:var(--total);text-align:right;padding-right:3px}
.heat .c1{background:var(--heat1)}.heat .c2{background:var(--heat2)}.heat .c3{background:var(--heat3)}.heat .c4{background:var(--heat4)}.heat .c5{background:var(--heat5)}
.yearly{position:absolute;left:464px;top:675px;width:77px;border-collapse:collapse;font-size:5px;table-layout:fixed}
.yearly td{border:1px solid var(--grid);height:14px;padding:0 3px;white-space:nowrap}
.yearly td:last-child{background:var(--total);text-align:right}
.footer-rule{position:absolute;left:0;top:705px;width:575px;height:4px;background:linear-gradient(to right,#bbb,#e2e2e2)}
.brand-left{position:absolute;left:36px;top:730px;display:flex;align-items:center;gap:8px}
.brand-dot{width:26px;height:26px;border-radius:50%;background:var(--orange)}
.brand-name{font-size:28px;font-weight:700;color:var(--orange);line-height:1}
.brand-tag{position:absolute;left:70px;top:764px;font-size:9px;color:#444}
.contact{position:absolute;left:251px;top:734px;font-size:14px;line-height:18px}
.contact strong{font-style:italic;font-size:14px}
.photo{position:absolute;inset:0;background:linear-gradient(170deg,#2d6cb6 0%,#6f9fd2 22%,#dbe5ee 38%,#2f3f6e 48%,#23335f 62%,#7e8898 78%,#c9ccd0 100%)}
.swoosh{position:absolute;left:0;top:0}
.brand-right{position:absolute;left:305px;top:648px;display:flex;align-items:center;gap:10px}
.brand-right .brand-dot{width:34px;height:34px;background:var(--yellow)}
.brand-right .brand-name{color:#fff;font-size:36px}
.brand-right-tag{position:absolute;left:372px;top:694px;font-size:12px;color:#fff}
.caption{position:absolute;right:16px;top:758px;text-align:right;color:#fff;font-size:14px;line-height:18px}
</style>
</head>
<body>
<div class="spread">
  <section class="page-left">
    <h2 class="section-title config-title">Solar Generator configuration options</h2>
    <table class="config-table">
      <colgroup><col style="width:149px"><col style="width:113px"><col style="width:120px"><col style="width:115px"></colgroup>
      <tr><th style="border:none"></th><th>Single block</th><th>Full 20' container</th><th>Full 40' container</th></tr>
      <tr><td>Solar generator capacity<br>(kWp <sub>DC</sub>)<sup>1)</sup></td><td>24</td><td>72</td><td>168</td></tr>
      <tr><td>Peak output ( kW <sub>AC</sub> / kVA )</td><td>20</td><td>60</td><td>140</td></tr>
      <tr><td>Avg. energy generation <sup>2)</sup></td><td></td><td></td><td></td></tr>
      <tr><td class="indent">Daily min. (kWh <sub>AC</sub> / day)</td><td>96</td><td>288</td><td>672</td></tr>
      <tr><td class="indent">Daily max. (kWh <sub>AC</sub> / day)</td><td>120</td><td>360</td><td>840</td></tr>
      <tr><td class="indent">Annually min. (kWh <sub>AC</sub> / year)</td><td>35'040</td><td>105'120</td><td>245'280</td></tr>
      <tr><td class="indent">Annually max. (kWh <sub>AC</sub> / year)</td><td>43'800</td><td>131'400</td><td>306'600</td></tr>
      <tr><td>Module area (m2)</td><td>158</td><td>475</td><td>1'109</td></tr>
      <tr><td>Layout options <sup>3)</sup></td><td>50m x 4m (single row) /<br>25m x 12m (double row)</td><td>75m x 12 m (double row) /<br>50m x 20m (triple row)</td><td>75m x 36m (5 rows) /<br>50m x 52m (7 rows)</td></tr>
      <tr class="blank"><td></td><td></td><td></td><td></td></tr>
      <tr><td>Recommended minimum<br>diesel generator capacity (kVA)</td><td>~50</td><td>~100</td><td>~250</td></tr>
      <tr><td>Battery capacity</td><td colspan="3">up to 24h (on request)</td></tr>
    </table>
    <ul class="notes">
      <li>Other capacities are available in multiples of 24 kWp</li>
      <li>Typical range up to 30° latitude. Actual output depends on the exact location</li>
      <li>Other layouts available on request</li>
    </ul>
    <h2 class="section-title daily-title">Typical energy generation during the day</h2>
    <p class="block-label">Standard 24 kWp Solar Generator block</p>
    <p class="kwh-label">Solar kWh</p>
    <table class="heat">
      <colgroup><col style="width:30px"><col span="24" style="width:17.5px"><col style="width:60px"></colgroup>
      <tr><th class="month time">Time</th><th>00:00</th><th>01:00</th><th>02:00</th><th>03:00</th><th>04:00</th><th>05:00</th><th>06:00</th><th>07:00</th><th>08:00</th><th>09:00</th><th>10:00</th><th>11:00</th><th>12:00</th><th>13:00</th><th>14:00</th><th>15:00</th><th>16:00</th><th>17:00</th><th>18:00</th><th>19:00</th><th>20:00</th><th>21:00</th><th>22:00</th><th>23:00</th><th class="sum">Monthly Total</th></tr>
      <tr><td class="month">January</td><td>0.0</td><td>0.0</td><td>0.0</td><td>0.0</td><td>0.0</td><td>0.0</td><td>0.0</td><td>0.0</td><td class="c1">0.9</td><td class="c2">4.1</td><td class="c3">8.0</td><td class="c3">11.7</td><td class="c4">12.8</td><td class="c5">15.5</td><td class="c4">14.4</td><td class="c3">11.7</td><td class="c3">8.7</td><td class="c2">4.6</td><td class="c1">1.2</td><td>0.0</td><td>0.0</td><td>0.0</td><td>0.0</td><td>0.0</td><td class="sum">2'931</td></tr>
      <tr><td class="month">February</td><td>0.0</td><td>0.0</td><td>0.0</td><td>0.0</td><td>0.0</td><td>0.0</td><td>0.0</td><td>0.0</td><td class="c1">1.7</td><td class="c2">6.2</td><td class="c3">10.6</td><td class="c4">14.1</td><td class="c5">16.3</td><td class="c5">17.2</td><td class="c5">16.2</td><td class="c4">13.9</td><td class="c3">10.4</td><td class="c2">5.9</td><td class="c1">1.7</td><td>0.0</td><td>0.0</td><td>0.0</td><td>0.0</td><td>0.0</td><td class="sum">3'196</td></tr>
      <tr><td class="month">March</td><td>0.0</td><td>0.0</td><td>0.0</td><td>0.0</td><td>0.0</td><td>0.0</td><td>0.0</td><td class="c1">0.2</td><td class="c1">2.9</td><td class="c2">7.4</td><td class="c3">11.3</td><td class="c4">14.3</td><td class="c5">16.2</td><td class="c5">16.9</td><td class="c5">15.6</td><td class="c4">13.8</td><td class="c3">10.8</td><td class="c2">6.6</td><td class="c1">2.3</td><td>0.0</td><td>0.0</td><td>0.0</td><td>0.0</td><td>0.0</td><td class="sum">3'665</td></tr>
      <tr><td class="month">April</td><td>0.0</td><td>0.0</td><td>0.0</td><td>0.0</td><td>0.0</td><td>0.0</td><td>0.0</td><td class="c1">1.3</td><td class="c2">5.1</td><td class="c3">9.1</td><td class="c4">12.9</td><td class="c5">16.2</td><td class="c5">17.6</td><td class="c5">18.3</td><td class="c5">17.7</td><td class="c5">15.8</td><td class="c4">12.2</td><td class="c2">7.9</td><td class="c2">3.4</td><td class="c1">0.3</td><td>0.0</td><td>0.0</td><td>0.0</td><td>0.0</td><td class="sum">4'130</td></tr>
      <tr><td class="month">May</td><td>0.0</td><td>0.0</td><td>0.0</td><td>0.0</td><td>0.0</td><td>0.0</td><td>0.0</td><td class="c1">2.3</td><td class="c2">6.3</td><td class="c3">10.4</td><td class="c4">13.6</td><td class="c5">15.9</td><td class="c5">17.4</td><td class="c5">17.9</td><td class="c5">17.0</td><td class="c5">15.2</td><td class="c4">12.3</td><td class="c3">8.4</td><td class="c2">4.1</td><td class="c1">0.7</td><td>0.0</td><td>0.0</td><td>0.0</td><td>0.0</td><td class="sum">4'390</td></tr>
      <tr><td class="month">June</td><td>0.0</td><td>0.0</td><td>0.0</td><td>0.0</td><td>0.0</td><td>0.0</td><td class="c1">0.2</td><td class="c1">2.4</td><td class="c2">6.0</td><td class="c3">9.6</td><td class="c4">12.3</td><td class="c4">14.4</td><td class="c5">15.8</td><td class="c5">16.3</td><td class="c5">15.8</td><td class="c4">14.1</td><td class="c3">11.5</td><td class="c3">8.0</td><td class="c2">4.3</td><td class="c1">1.1</td><td>0.0</td><td>0.0</td><td>0.0</td><td>0.0</td><td class="sum">3'958</td></tr>
      <tr><td class="month">July</td><td>0.0</td><td>0.0</td><td>0.0</td><td>0.0</td><td>0.0</td><td>0.0</td><td>0.0</td><td class="c1">1.6</td><td class="c2">4.8</td><td class="c3">8.4</td><td class="c3">11.6</td><td class="c4">14.5</td><td class="c5">16.0</td><td class="c5">16.4</td><td class="c5">16.0</td><td class="c4">14.2</td><td class="c3">11.3</td><td class="c2">7.7</td><td class="c2">4.0</td><td class="c1">1.0</td><td>0.0</td><td>0.0</td><td>0.0</td><td>0.0</td><td class="sum">3'953</td></tr>
      <tr><td class="month">August</td><td>0.0</td><td>0.0</td><td>0.0</td><td>0.0</td><td>0.0</td><td>0.0</td><td>0.0</td><td class="c1">1.2</td><td class="c2">4.7</td><td class="c3">8.7</td><td class="c4">12.2</td><td class="c4">14.8</td><td class="c5">16.5</td><td class="c5">17.0</td><td class="c5">16.2</td><td class="c4">14.1</td><td class="c3">11.3</td><td class="c2">7.5</td><td class="c2">3.4</td><td class="c1">0.6</td><td>0.0</td><td>0.0</td><td>0.0</td><td>0.0</td><td class="sum">3'977</td></tr>
      <tr><td class="month">September</td><td>0.0</td><td>0.0</td><td>0.0</td><td>0.0</td><td>0.0</td><td>0.0</td><td>0.0</td><td class="c1">0.9</td><td class="c2">4.6</td><td class="c3">9.0</td><td class="c4">12.7</td><td class="c5">15.4</td><td class="c5">16.9</td><td class="c5">17.2</td><td class="c5">16.3</td><td class="c4">14.1</td><td class="c3">10.9</td><td class="c2">6.7</td><td class="c1">2.2</td><td>0.0</td><td>0.0</td><td>0.0</td><td>0.0</td><td>0.0</td><td class="sum">3'808</td></tr>
      <tr><td class="month">October</td><td>0.0</td><td>0.0</td><td>0.0</td><td>0.0</td><td>0.0</td><td>0.0</td><td>0.0</td><td class="c1">0.8</td><td class="c2">3.9</td><td class="c3">8.4</td><td class="c4">12.1</td><td class="c4">14.9</td><td class="c5">16.4</td><td class="c5">16.4</td><td class="c5">15.3</td><td class="c4">12.8</td><td class="c3">8.9</td><td class="c2">4.3</td><td class="c1">0.9</td><td>0.0</td><td>0.0</td><td>0.0</td><td>0.0</td><td>0.0</td><td class="sum">3'455</td></tr>
      <tr><td class="month">November</td><td>0.0</td><td>0.0</td><td>0.0</td><td>0.0</td><td>0.0</td><td>0.0</td><td>0.0</td><td>0.0</td><td class="c1">2.8</td><td class="c2">7.1</td><td class="c3">10.8</td><td class="c4">13.5</td><td class="c5">15.3</td><td class="c5">15.2</td><td class="c4">14.0</td><td class="c3">11.7</td><td class="c2">7.8</td><td class="c2">3.1</td><td class="c1">0.1</td><td>0.0</td><td>0.0</td><td>0.0</td><td>0.0</td><td>0.0</td><td class="sum">3'042</td></tr>
      <tr><td class="month">December</td><td>0.0</td><td>0.0</td><td>0.0</td><td>0.0</td><td>0.0</td><td>0.0</td><td>0.0</td><td>0.0</td><td class="c1">1.6</td><td class="c2">5.1</td><td class="c3">8.9</td><td class="c3">11.4</td><td class="c4">12.6</td><td class="c4">12.7</td><td class="c4">12.0</td><td class="c3">10.1</td><td class="c2">6.6</td><td class="c1">2.5</td><td>0.0</td><td>0.0</td><td>0.0</td><td>0.0</td><td>0.0</td><td>0.0</td><td class="sum">2'591</td></tr>
    </table>
    <table class="yearly">
      <colgroup><col style="width:32px"><col style="width:45px"></colgroup>
      <tr><td>Yearly Total</td><td>43'096</td></tr>
    </table>
    <div class="footer-rule"></div>
    <div class="brand-left"><span class="brand-dot"></span><span class="brand-name">Solvantix</span></div>
    <p class="brand-tag">Clean Power. Every Site.</p>
    <p class="contact"><strong>For more information, Contact us at</strong><br>Contact Us : +971 4 555 0182<br>Log On : www.solvantix.com or</p>
  </section>

  <section class="page-right">
    <div class="photo" role="img" aria-label="Rows of tilted solar panels on aluminium racking against a blue sky with white clouds"></div>
    <svg class="swoosh" width="570" height="813" viewBox="0 0 570 813" aria-hidden="true">
      <defs>
        <linearGradient id="darkBand" x1="0" y1="0" x2="0" y2="1">
          <stop offset="0" stop-color="#555"/>
          <stop offset="0.4" stop-color="#2e2e2e"/>
          <stop offset="1" stop-color="#1b1b1b"/>
        </linearGradient>
      </defs>
      <path d="M0 640 Q280 560 570 572 L570 813 L0 813 Z" fill="#f4f4f4"/>
      <path d="M0 655 Q280 585 570 592 L570 813 L0 813 Z" fill="url(#darkBand)"/>
      <path d="M0 735 Q250 632 570 598 L570 616 Q270 648 0 770 Z" fill="var(--yellow)"/>
    </svg>
    <div class="brand-right"><span class="brand-dot"></span><span class="brand-name">Solvantix</span></div>
    <p class="brand-right-tag">Clean Power. Every Site.</p>
    <p class="caption">Solvantix solar hybrid systems<br>Cheaper and cleaner energy than diesel generators</p>
  </section>
</div>
</body>
</html>
```